Gannet Rumpus Web Design Theme Ideas

I have a new golf website that I am designing. It will be a website where a group of golfers can track their scores and results as a small tournament. The site will allow side matches between players. These players are referred to as "Pigeons". The side matches are what I refer to as "Chaos". But, I would rather spell it "Khaos". Looking for some good ideas for a crazy looking pigeon themed golfer. The definition of a "pigeon" in golf is a golfer who is not that good but thinks they are good. Obviously, "chaos" is disorderly confusion.

Target Market(s)

Golfers who like to gamble with other golfers

Industry/Entity Type

Golf

Number of Pages Required

5+ page

Font styles to use
Sans Serif

Requirements
Must have
• Pigeons, golf theme
Should not have
• the words gamble, bet, wager

```html
<!DOCTYPE html>
<html lang="en">
<head>
<meta charset="utf-8">
<title>Gannet Rumpus</title>
<link rel="stylesheet" href="https://fonts.googleapis.com/css2?family=Roboto:wght@300;400;500;700&family=Allura&display=swap">
<style>
:root{
  --green:#0f8a2a;
  --green-dark:#0b6e21;
  --lime:#8cc63f;
  --gallery:#7cbb37;
  --pale:#dbe6de;
  --text:#555;
  --ink:#222;
  --row:#f3f8ec;
  --head:#cfd1cf;
}
*{box-sizing:border-box;margin:0;padding:0}
html,body{width:1200px;height:3566px;overflow:hidden}
body{position:relative;background:#fff;font-family:'Roboto',sans-serif;color:var(--text)}
.abs{position:absolute}
.script{font-family:'Allura',cursive;color:var(--green);font-weight:400}
.brand{font-family:'Roboto',sans-serif;font-weight:500;color:var(--green);font-size:26px}
/* nav */
.site-nav{top:0;left:0;width:1200px;height:90px;background:#fff}
.site-nav .brand{left:111px;top:28px}
.nav-links a{position:absolute;top:36px;font-size:14px;color:#333;text-decoration:none}
.nav-links a.active{color:var(--green)}
.btn{display:flex;align-items:center;justify-content:center;border-radius:22px;font-family:'Allura',cursive;font-size:24px;color:#fff;background:var(--green)}
.btn-outline{background:transparent;border:2px solid var(--green);color:var(--green)}
/* hero */
.hero{top:90px;left:0;width:1200px;height:595px;background:linear-gradient(180deg,#d4dc86 0%,#a9c751 35%,#66a526 70%,#3f861a 100%)}
.hero-title{left:109px;top:248px;font-size:66px;color:var(--green);letter-spacing:1px;white-space:nowrap}
.hero-title .strong{font-weight:700}
.hero-title .light{font-weight:300}
.dots span{position:absolute;top:581px;width:14px;height:14px;border-radius:50%;background:#fff}
/* about */
.about-photo{left:205px;top:775px;width:307px;height:380px;border-radius:6px;background:linear-gradient(180deg,#2a2f24 0%,#3c4a2c 50%,#5d8f32 100%)}
.section-title{font-size:64px;text-align:center;width:1200px;left:0}
.about-text{left:605px;top:874px;width:482px;font-size:15.5px;line-height:26px;color:#666}
/* services */
.services{top:1245px;left:0;width:1200px;height:598px;background:var(--pale)}
.card{overflow:hidden}
.card .label{position:absolute;bottom:22px;left:0;font-weight:700;font-size:22px;color:#fff}
.card-side{top:1449px;height:271px;width:321px}
.card-main{left:322px;top:1414px;width:554px;height:340px;border:5px solid #fff;border-radius:22px;box-shadow:0 4px 14px rgba(0,0,0,.25);background:linear-gradient(180deg,#5c8f2c,#88b84a 60%,#a7cc6a)}
.arrow{width:38px;height:38px;border-radius:50%;border:2px solid #fff;display:flex;align-items:center;justify-content:center;background:rgba(0,0,0,.25)}
/* duffers */
.table-box{left:152px;top:2057px;width:896px;height:469px;background:#fff;box-shadow:0 2px 12px rgba(0,0,0,.12)}
.filters{position:absolute;left:0;top:0;width:896px;height:98px;background:var(--green)}
.field{position:absolute;top:23px;height:50px;background:#21953a;color:#cfe7cf;font-size:14px;display:flex;align-items:center;padding:0 20px;justify-content:space-between}
.field.search{background:var(--lime);border-radius:25px;color:#fff;font-weight:700}
.thead{position:absolute;top:98px;left:0;width:896px;height:42px;background:var(--head);font-size:17px;font-weight:500;color:#222}
.thead span,.trow span{position:absolute}
.trow{position:absolute;left:0;width:896px;height:50.5px;font-size:13.5px;color:#222}
.trow:nth-child(even){background:var(--row)}
/* gallery */
.gallery{top:2695px;left:0;width:1200px;height:506px;background:linear-gradient(180deg,#86c23f,#6fae2d)}
.gallery .section-title{color:#fff;top:60px}
.shot{top:171px;width:231px;height:241px;border-radius:4px}
/* footer */
.footer .brand{left:0;width:1200px;text-align:center;top:3302px}
.footer-links a{position:absolute;top:3367px;font-size:15px;color:#333;text-decoration:none}
.contact{top:3414px;left:0;width:1200px;display:flex;justify-content:center;gap:20px;font-size:15px;color:#444;align-items:center}
.contact .sep{color:#bbb}
.contact svg{vertical-align:-3px;margin-right:8px}
.social{top:3468px;left:0;width:1200px;display:flex;justify-content:center;gap:30px}
.social span{width:16px;height:16px;border-radius:50%;background:var(--lime)}
.copy{top:3518px;left:0;width:1200px;text-align:center;font-size:15px;color:#444}
</style>
</head>
<body>

<header class="abs site-nav">
  <div class="abs brand">Gannet Rumpus</div>
  <nav class="nav-links">
    <a class="active" style="left:462px">Home</a>
    <a style="left:549px">About Us</a>
    <a style="left:655px">Services</a>
    <a style="left:757px">Blog</a>
    <a style="left:833px">Contact</a>
  </nav>
  <div class="abs btn" style="left:963px;top:24px;width:125px;height:42px">Register</div>
</header>

<section class="abs hero" role="img" aria-label="Golf iron and ball on sunlit fairway grass, with a white pigeon flying above the title"></section>
<h1 class="abs hero-title"><span class="strong">GANNET</span> <span class="light">RUMPUS</span></h1>
<div class="abs btn btn-outline" style="left:112px;top:361px;width:125px;height:44px">Register</div>
<div class="dots">
  <span style="left:567px"></span>
  <span style="left:589px;top:576px;width:24px;height:24px;border:4px solid #fff;background:var(--green)"></span>
  <span style="left:619px"></span>
</div>
<svg class="abs" style="left:0;top:585px" width="1200" height="110" viewBox="0 0 1200 110">
  <path d="M0 95 C180 20 360 15 600 45 C840 75 1000 80 1200 20 L1200 110 L0 110 Z" fill="#fff"/>
  <path d="M0 92 C180 17 360 12 600 42 C840 72 1000 77 1200 17" fill="none" stroke="#4d9a25" stroke-width="3"/>
</svg>

<section class="about">
  <div class="abs about-photo" role="img" aria-label="Pigeon silhouette framing a golf ball and club on grass"></div>
  <h2 class="abs script" style="left:605px;top:768px;font-size:66px">About Us</h2>
  <p class="abs about-text">Lorem ipsum dolor sit amet, consectetur adipiscing elit, sed do eiusmod tempor incididunt ut labore et dolore magna aliqua. Ut enim ad minim veniam, quis nostrud exercitation ullamco laboris nisi ut aliquip ex ea commodo consequat. Duis aute irure dolor in reprehenderit in voluptate velit esse cillum dolore eu fugiat nulla pariatur. Excepteur sint occaecat cupidatat non proident, sunt in culpa qui officia deserunt mollit anim id est laborum.</p>
  <div class="abs btn" style="left:606px;top:1090px;width:124px;height:45px">Learn More</div>
</section>

<section class="abs services"></section>
<h2 class="abs script section-title" style="top:1290px">Our Services</h2>
<div class="abs card card-side" style="left:0;background:linear-gradient(135deg,#2c3a1c,#4d6a2a 60%,#1f2a12)" role="img" aria-label="Golf clubs in a bag"><span class="label">LOREM IPSUM</span></div>
<div class="abs card card-side" style="left:879px;background:linear-gradient(135deg,#3a2a18,#6b7a3a 60%,#2f3a18)" role="img" aria-label="Golf ball on a tee"><span class="label" style="left:15px">LOREM IPSUM</span></div>
<div class="abs card card-main" role="img" aria-label="Golfer carrying a golf bag across the course"><span class="label" style="left:30px;font-size:24px">LOREM IPSUM</span></div>
<div class="abs arrow" style="left:123px;top:1560px"><svg width="14" height="14" viewBox="0 0 14 14"><path d="M9 2 L4 7 L9 12" fill="none" stroke="#fff" stroke-width="2"/></svg></div>
<div class="abs arrow" style="left:1039px;top:1560px"><svg width="14" height="14" viewBox="0 0 14 14"><path d="M5 2 L10 7 L5 12" fill="none" stroke="#fff" stroke-width="2"/></svg></div>

<h2 class="abs script section-title" style="top:1912px">Our Duffers</h2>
<div class="abs table-box">
  <div class="filters">
    <div class="field" style="left:28px;width:198px">Country <span>&#8964;</span></div>
    <div class="field" style="left:242px;width:197px">State <span>&#8964;</span></div>
    <div class="field" style="left:457px;width:196px">First Name</div>
    <div class="field search" style="left:670px;width:198px">Finch
      <svg width="13" height="13" viewBox="0 0 13 13"><circle cx="5.5" cy="5.5" r="4" fill="none" stroke="#fff" stroke-width="2"/><path d="M8.5 8.5 L12 12" stroke="#fff" stroke-width="2"/></svg></div>
  </div>
  <div class="thead"><span style="left:46px;top:11px">Name</span><span style="left:357px;top:11px">Club</span><span style="left:702px;top:11px">Handicap Index</span></div>
  <div style="position:absolute;top:140px;left:0">
    <div class="trow" style="top:0"><span style="left:46px;top:14px">Arlo Finch</span><span style="left:357px;top:18px">Cedar Hollow Mens Golf Club</span><span style="left:702px;top:16px">NH</span></div>
    <div class="trow" style="top:50.5px"><span style="left:46px;top:14px">Arlo Finch</span><span style="left:357px;top:18px">Maple Ridge Country Club</span><span style="left:702px;top:8px">20.2</span></div>
    <div class="trow" style="top:101px"><span style="left:46px;top:14px">Arlo Finch</span><span style="left:357px;top:18px">Links Club Harbor Bay</span><span style="left:702px;top:0">1.1</span></div>
    <div class="trow" style="top:151.5px"><span style="left:46px;top:14px">Arlo Finch</span><span style="left:357px;top:18px">Tee Circle Valley Alumni</span><span style="left:702px;top:-8px">1.1</span><span style="left:702px;top:34px">11.1</span></div>
    <div class="trow" style="top:202px"><span style="left:46px;top:14px">Arlo Finch</span><span style="left:357px;top:18px">Links Club North Cove</span><span style="left:702px;top:26px">13.2</span></div>
    <div class="trow" style="top:252.5px"><span style="left:46px;top:14px">Arlo Finch</span><span style="left:357px;top:18px">Links Club Bayview</span><span style="left:702px;top:16px">21.4</span></div>
  </div>
</div>
<div class="abs btn" style="left:538px;top:2565px;width:124px;height:44px">Load More</div>

<section class="abs gallery">
  <h2 class="abs script section-title">Our Gallery</h2>
  <div class="abs shot" style="left:111px;background:linear-gradient(160deg,#6f8a5a,#24324a 60%,#8aa24a)" role="img" aria-label="Golfer in a cap mid swing"></div>
  <div class="abs shot" style="left:360px;background:linear-gradient(180deg,#142a0e,#2b5a18 60%,#3f7a22)" role="img" aria-label="Golf ball on a tee in grass"></div>
  <div class="abs shot" style="left:609px;background:linear-gradient(180deg,#7a5a4a,#d89a4a 30%,#3f6a2a 50%,#6ea23a)" role="img" aria-label="Golf course at sunset with bunker and trees"></div>
  <div class="abs shot" style="left:858px;background:linear-gradient(180deg,#f1eee4,#dfe2cf 60%,#b7cf8a)" role="img" aria-label="Golfer and golf cart in morning fog"></div>
</section>

<footer class="footer">
  <div class="abs brand">Gannet Rumpus</div>
  <nav class="footer-links">
    <a style="left:422px">Home</a>
    <a style="left:491px">About Us</a>
    <a style="left:580px">Services</a>
    <a style="left:665px">Blog</a>
    <a style="left:722px">Contact</a>
  </nav>
  <div class="abs contact">
    <span><svg width="14" height="14" viewBox="0 0 14 14"><path d="M3 1 L5.5 1 L6.5 4 L5 5.5 C6 7.5 7 8.5 8.5 9 L10 7.5 L13 8.5 L13 11 C13 12 12 13 11 13 C5.5 12.5 1.5 8.5 1 3 C1 2 2 1 3 1 Z" fill="var(--lime)"/></svg>+1 (888) 888 8888</span>
    <span class="sep">|</span>
    <span><svg width="16" height="12" viewBox="0 0 16 12"><rect width="16" height="12" rx="1" fill="var(--lime)"/><path d="M1 1 L8 7 L15 1" fill="none" stroke="#fff" stroke-width="1.5"/></svg>info@gannetrumpus.com</span>
    <span class="sep">|</span>
    <span><svg width="12" height="16" viewBox="0 0 12 16"><path d="M6 0 C9.3 0 12 2.6 12 6 C12 10 6 16 6 16 C6 16 0 10 0 6 C0 2.6 2.7 0 6 0 Z" fill="var(--lime)"/><circle cx="6" cy="6" r="2.3" fill="#fff"/></svg>Lorem ipsum dolor sit amet,</span>
  </div>
  <div class="abs social" aria-label="Social links">
    <span></span><span></span><span></span><span></span>
  </div>
  <p class="abs copy">Copyrights 2023 Gannet Rumpus &nbsp;|&nbsp;&nbsp; All Rights Reserved</p>
</footer>

</body>
</html>
```